Scientific Web Site for TALQUIRE

Professional Scientific / Service orientated web site, motto, new logos attached for viewing.

"We measure so the Business Owner can Manage" their environments.
Site needs to be be mobile friendly.

We provide a service to electronically measure cleanliness of any surface and a value added disinfecting fogging surface.

Reports showing locations, trending, tracking and randomized test plans ongoing audits will be made available..

NOTE: Although image of Corona Virus is current we don't wont it plastered through the web site, their is more than the current virus.

Home Page - Professional Scientific / Service Looking
About
Our Approach
Services
Residential
Commercial
Transportation
Gyms
Educational & Daycare
Real Estate - Open for inspections, End of Lease etc

Contact
Mobile #
Email
Form to leave their details

Links to social media, Facebook, Instagram
Reference Sites: Ranked in preference
www.belunorm.com.au
https://www.vandrelhomecare.co.uk/
https://www.zelmarup.com/
https://www.ortivane.com.au/specialist-surface-disinfection/
https://www.plakorniv.com/design/48102937
https://www.plakorniv.com/design/59730418
https://www.plakorniv.com/design/41867205

Target Market(s)

Commercial and professional Services

Font styles to use
Sans Serif

Requirements
Must have
• Wix Website
Clean fresh look with appropriate imaging
Web site is a company advertising that will hold static information and we will market through social media.
Nice to have
• Scientific look and feel
Should not have
• Prominent Corona Virus images or references

```html
<!DOCTYPE html>
<html lang="en">
<head>
<meta charset="utf-8">
<title>Talquire — Disinfectant Fogging Services</title>
<link rel="stylesheet" href="https://fonts.googleapis.com/css2?family=Montserrat:wght@500;600;700&family=Raleway:wght@300;400;500&family=Playfair+Display&display=swap">
<style>
:root{
  --orange:#f58220;
  --dark:#1e1e1e;
  --footer:#2a2a2a;
  --ink:#222;
  --muted:#666;
  --light:#f6f6f6;
  --white:#fff;
}
*{box-sizing:border-box;margin:0;padding:0}
html,body{width:1200px;height:3421px;overflow:hidden}
body{font-family:'Raleway',sans-serif;color:var(--ink);background:var(--white);position:relative}
.abs{position:absolute}
.btn{position:absolute;background:var(--orange);color:#fff;font:700 12px 'Montserrat',sans-serif;text-transform:uppercase;display:flex;align-items:center;justify-content:center;letter-spacing:.3px}
.topbar{position:absolute;top:0;left:0;width:1200px;height:26px;background:var(--orange);color:#fff;font:400 11px 'Raleway',sans-serif}
.topbar .social{position:absolute;left:92px;top:7px;display:flex;gap:9px}
.topbar .social span{width:11px;height:11px;border-radius:50%;border:1.5px solid #fff}
.topbar .contact{position:absolute;right:94px;top:6px;display:flex;gap:26px;align-items:center}
.topbar .contact b{font-weight:700}
.topbar svg{vertical-align:-2px;margin-right:3px}
.nav{position:absolute;top:26px;left:0;width:1200px;height:67px;background:#fff}
.brand{position:absolute;left:93px;top:20px;display:flex;align-items:center;gap:8px;font:600 19px 'Montserrat',sans-serif;letter-spacing:2px;color:var(--ink)}
.brand i{width:14px;height:14px;background:var(--orange)}
.menu{position:absolute;right:94px;top:27px;display:flex;gap:26px;font:400 11px 'Raleway',sans-serif;color:#444}
.menu .active{color:var(--orange)}
.hero{position:absolute;top:93px;left:0;width:1200px;height:507px;background:linear-gradient(100deg,#9aa2a6 0%,#c9cdcf 25%,#8a8e90 50%,#3e4042 80%,#2b2c2d 100%)}
.hero .pre{position:absolute;left:680px;top:156px;font:400 28px 'Playfair Display',serif;color:#fff}
.hero h1{position:absolute;left:680px;top:192px;font:700 46px/1.02 'Montserrat',sans-serif;color:#fff;text-transform:uppercase}
.welcome .eyebrow{position:absolute;left:93px;top:755px;font:400 16px 'Raleway',sans-serif}
.welcome h2{position:absolute;left:93px;top:775px;font:600 37px 'Montserrat',sans-serif;letter-spacing:.5px}
.welcome p{position:absolute;left:93px;top:832px;width:500px;font:400 13.5px/22.5px 'Raleway',sans-serif;color:var(--muted)}
.feature{position:absolute;top:1179px;left:0;width:1200px;height:388px}
.feature .eyebrow{position:absolute;left:617px;top:82px;font:400 16px 'Raleway',sans-serif;color:#fff}
.feature h2{position:absolute;left:617px;top:100px;font:600 37px/41px 'Montserrat',sans-serif;color:#fff;text-transform:uppercase}
.feature .tag{position:absolute;left:617px;top:192px;font:400 17px 'Raleway',sans-serif;color:var(--orange)}
.feature p{position:absolute;left:617px;top:225px;width:490px;font:400 12.5px/18px 'Raleway',sans-serif;color:#ddd}
.section-title{position:absolute;left:0;width:1200px;text-align:center;font:600 40px 'Montserrat',sans-serif;text-transform:uppercase;color:var(--ink)}
.service{position:absolute;width:300px;text-align:center}
.service .ring{position:relative;width:210px;height:206px;margin:0 auto}
.service .ring::before{content:"";position:absolute;left:4px;top:0;width:206px;height:206px;border-radius:50%;background:var(--orange)}
.service .photo{position:absolute;left:0;top:0;width:202px;height:206px;border-radius:50%;background:linear-gradient(135deg,#d9dcde,#8c9296 60%,#5c6064)}
.service h3{margin-top:22px;font:600 20px 'Montserrat',sans-serif;text-transform:uppercase}
.service p{margin-top:6px;font:400 12.5px/18px 'Raleway',sans-serif;color:var(--muted)}
.service .go{margin:10px auto 0;width:26px;height:26px;border-radius:50%;background:var(--orange);display:flex;align-items:center;justify-content:center}
.service .go.dark{background:#333}
.approach{position:absolute;width:240px;text-align:center}
.approach svg{display:block;margin:0 auto;height:50px}
.approach h4{margin-top:12px;font:600 19px 'Montserrat',sans-serif}
.approach p{margin-top:6px;font:400 12.5px/18px 'Raleway',sans-serif;color:var(--muted)}
.contact-band{position:absolute;top:2691px;left:0;width:1200px;height:464px;background:var(--light)}
.contact-band h2{position:absolute;top:60px;font:600 37px 'Montserrat',sans-serif}
.field{position:absolute;left:93px;width:445px;background:#fff;border:1px solid #c8c8c8;font:400 11px 'Raleway',sans-serif;color:#444;padding:11px 9px}
.video{position:absolute;left:625px;top:117px;width:481px;height:281px;background:linear-gradient(110deg,#3a3d42,#5d636a 35%,#2b2e33 70%,#1f2125)}
.video .play{position:absolute;left:216px;top:116px;width:48px;height:48px;border:2px solid #fff;border-radius:50%;display:flex;align-items:center;justify-content:center}
.footer{position:absolute;top:3155px;left:0;width:1200px;height:266px;background:var(--footer);color:#ddd}
.footer h5{position:absolute;top:34px;font:400 12.5px 'Raleway',sans-serif;text-transform:uppercase;color:#fff}
.footer ul{position:absolute;top:60px;list-style:none;font:400 10.5px/24px 'Raleway',sans-serif;color:#ccc}
.footer .addr{position:absolute;left:560px;top:60px;font:400 10.5px/14px 'Raleway',sans-serif;color:#ccc}
.footer .circles{position:absolute;left:560px;top:171px;display:flex;gap:5px}
.footer .circles span{width:24px;height:24px;border-radius:50%;background:#3d7fd0}
.map{position:absolute;left:795px;top:55px;width:311px;height:162px;background:linear-gradient(135deg,#e8e6e1,#d8dde3 50%,#ece9e4)}
.copy{position:absolute;left:93px;top:212px;font:400 10px 'Raleway',sans-serif;color:#999}
.copy b{color:#fff;font-weight:500}
</style>
</head>
<body>

<header class="topbar">
  <div class="social"><span></span><span></span><span></span></div>
  <div class="contact">
    <span><svg width="9" height="12" viewBox="0 0 9 12"><path d="M2 0h2l1 3-1.5 1c.5 1.5 1.5 3 3 3.8L7.5 7 9 9v2l-1 1C4 12 0 7 0 2z" fill="#fff"/></svg><b>PHONE:</b> +2 (555) 247 6190</span>
    <span><svg width="12" height="9" viewBox="0 0 12 9"><rect width="12" height="9" fill="#fff"/><path d="M0 0l6 5 6-5" stroke="#f58220" fill="none"/></svg><b>EMAIL:</b> info@talquire.com</span>
  </div>
</header>

<nav class="nav">
  <div class="brand"><i></i>Talquire</div>
  <div class="menu">
    <span class="active">Home</span><span>About</span><span>Our Approach</span><span>Services</span><span>Residential</span><span>Commercial</span><span>Transportation</span><span>Gyms</span><span>Educational &amp; Daycare</span><span>Real Estate</span>
  </div>
</nav>

<section class="hero" role="img" aria-label="Technician in a protective suit spraying disinfectant outside an apartment block">
  <div class="pre">We Provide</div>
  <h1>Disinfectant<br>Fogging Services</h1>
  <div class="btn" style="left:680px;top:305px;width:109px;height:37px">Get a Quote</div>
</section>

<section class="welcome">
  <div class="eyebrow">WELCOME TO</div>
  <h2>TALQUIRE</h2>
  <p>Sed ut perspiciatis unde omnis iste natus error sit voluptatem accusantium doloremque laudantium, totam rem aperiam, eaque ipsa quae ab illo inventore veritatis et quasi architecto beatae vitae dicta sunt explicabo. Nemo enim ipsam voluptatem quia voluptas sit aspernatur aut odit aut fugit, sed quia consequuntur magni dolores eos qui ratione voluptatem sequi nesciunt. Neque porro quisquam est, qui dolorem ipsum quia dolor sit amet</p>
  <div class="btn" style="left:93px;top:984px;width:93px;height:34px">Read More</div>
  <svg class="abs" style="left:610px;top:650px" width="500" height="480" viewBox="0 0 500 480">
    <rect x="135" y="115" width="270" height="270" rx="40" transform="rotate(45 270 250)" fill="none" stroke="#f58220" stroke-width="10"/>
    <rect x="120" y="100" width="260" height="260" rx="40" transform="rotate(45 250 230)" fill="#fff"/>
    <rect x="120" y="100" width="260" height="260" rx="40" transform="rotate(45 250 230)" fill="url(#lab)" role="img" aria-label="Scientists in a lab using a microscope"/>
    <defs><linearGradient id="lab" x1="0" y1="0" x2="1" y2="1"><stop offset="0" stop-color="#eef1f3"/><stop offset=".5" stop-color="#bfd2de"/><stop offset="1" stop-color="#e3e7ea"/></linearGradient></defs>
  </svg>
</section>

<section class="feature">
  <svg class="abs" style="left:0;top:0" width="1200" height="388">
    <rect x="0" y="29" width="1200" height="359" fill="#1e1e1e"/>
    <polygon points="0,0 420,0 620,388 0,388" fill="url(#room)" role="img" aria-label="Technician in protective suit fogging a bright room"/>
    <defs><linearGradient id="room" x1="0" y1="0" x2="1" y2="1"><stop offset="0" stop-color="#e4e2de"/><stop offset=".6" stop-color="#c9c3bb"/><stop offset="1" stop-color="#a88a6a"/></linearGradient></defs>
  </svg>
  <div class="eyebrow">WE PROVIDE</div>
  <h2>Electronically<br>Measure Cleanliness</h2>
  <div class="tag">Any surface and a value added disinfecting fogging surface.</div>
  <p>Sed ut perspiciatis unde omnis iste natus error sit voluptatem accusantium doloremque laudantium, totam rem aperiam, eaque ipsa quae ab illo inventore veritatis et quasi architecto beatae vitae dicta sunt explicabo.</p>
  <div class="btn" style="left:617px;top:298px;width:93px;height:34px">Read More</div>
</section>

<h2 class="section-title" style="top:1610px">Disinfection Services</h2>

<div class="service" style="left:112px;top:1681px"><div class="ring"><div class="photo" role="img" aria-label="Technician disinfecting a home interior"></div></div><h3>Residential</h3><p>Sed ut perspiciatis unde omnis iste<br>error sit voluptatem accusantium doloremque</p><div class="go"><svg width="10" height="10"><path d="M1 5h7M5 2l3 3-3 3" stroke="#fff" stroke-width="1.6" fill="none"/></svg></div></div>
<div class="service" style="left:449px;top:1681px"><div class="ring"><div class="photo" role="img" aria-label="Technician fogging an office"></div></div><h3>Commercial</h3><p>Sed ut perspiciatis unde omnis iste<br>error sit voluptatem accusantium doloremque</p><div class="go"><svg width="10" height="10"><path d="M1 5h7M5 2l3 3-3 3" stroke="#fff" stroke-width="1.6" fill="none"/></svg></div></div>
<div class="service" style="left:786px;top:1681px"><div class="ring"><div class="photo" role="img" aria-label="Technician disinfecting gym equipment"></div></div><h3>Gym</h3><p>Sed ut perspiciatis unde omnis iste<br>error sit voluptatem accusantium doloremque</p><div class="go"><svg width="10" height="10"><path d="M1 5h7M5 2l3 3-3 3" stroke="#fff" stroke-width="1.6" fill="none"/></svg></div></div>

<div class="service" style="left:112px;top:2027px"><div class="ring"><div class="photo" style="background:linear-gradient(135deg,#a9c6ea,#3f6fb8 60%,#24467f)" role="img" aria-label="Technician disinfecting a classroom"></div></div><h3>Educational &amp; Daycare</h3><p>Sed ut perspiciatis unde omnis iste<br>error sit voluptatem accusantium doloremque</p><div class="go dark"><svg width="10" height="10"><path d="M1 5h7M5 2l3 3-3 3" stroke="#fff" stroke-width="1.6" fill="none"/></svg></div></div>
<div class="service" style="left:449px;top:2027px"><div class="ring"><div class="photo" role="img" aria-label="Technician disinfecting a transport station"></div></div><h3>Transportation</h3><p>Sed ut perspiciatis unde omnis iste<br>error sit voluptatem accusantium doloremque</p><div class="go dark"><svg width="10" height="10"><path d="M1 5h7M5 2l3 3-3 3" stroke="#fff" stroke-width="1.6" fill="none"/></svg></div></div>
<div class="service" style="left:786px;top:2027px"><div class="ring"><div class="photo" role="img" aria-label="Technician disinfecting an outdoor property"></div></div><h3>Real Estate</h3><p>Sed ut perspiciatis unde omnis iste<br>error sit voluptatem accusantium doloremque</p><div class="go dark"><svg width="10" height="10"><path d="M1 5h7M5 2l3 3-3 3" stroke="#fff" stroke-width="1.6" fill="none"/></svg></div></div>

<h2 class="section-title" style="top:2420px">Our Approach</h2>

<div class="approach" style="left:100px;top:2487px">
  <svg viewBox="0 0 30 50" width="30"><text x="15" y="42" text-anchor="middle" font-family="Montserrat,sans-serif" font-weight="700" font-size="46" fill="#f58220">$</text></svg>
  <h4>More Effective</h4><p>Sed ut perspiciatis unde omnis iste<br>natus error...</p>
</div>
<div class="approach" style="left:354px;top:2487px">
  <svg viewBox="0 0 60 50" width="60"><path d="M2 19h12M6 25h10M2 31h12" stroke="#f58220" stroke-width="3"/><circle cx="38" cy="25" r="18" fill="#f58220"/><circle cx="38" cy="25" r="13" fill="#fff"/><path d="M38 15v10l7 4" stroke="#f58220" stroke-width="2.5" fill="none"/></svg>
  <h4>Fast</h4><p>Sed ut perspiciatis unde omnis iste<br>natus error...</p>
</div>
<div class="approach" style="left:607px;top:2487px">
  <svg viewBox="0 0 54 50" width="54"><path d="M6 44C6 20 22 8 50 8c0 26-14 38-38 36z" fill="#f58220"/><path d="M6 44L38 20" stroke="#fff" stroke-width="2.5"/></svg>
  <h4>Environmental</h4><p>Sed ut perspiciatis unde omnis iste<br>natus error...</p>
</div>
<div class="approach" style="left:861px;top:2487px">
  <svg viewBox="0 0 50 50" width="50"><path d="M4 24L25 6l21 18h-6v22H10V24z" fill="#f58220"/><rect x="15" y="28" width="8" height="8" fill="#fff"/><rect x="27" y="30" width="7" height="16" fill="#fff"/></svg>
  <h4>Safe</h4><p>Sed ut perspiciatis unde omnis iste<br>natus error...</p>
</div>

<section class="contact-band">
  <h2 style="left:93px">For Queries</h2>
  <div class="field" style="top:120px;height:34px">Name:</div>
  <div class="field" style="top:160px;height:33px">Email:</div>
  <div class="field" style="top:199px;height:33px">Phone:</div>
  <div class="field" style="top:240px;height:111px;width:442px">Comments:</div>
  <div class="btn" style="left:93px;top:363px;width:95px;height:35px">Submit</div>
  <h2 style="left:625px">Fogging in Action</h2>
  <div class="video" role="img" aria-label="Video of a technician fogging a dark interior">
    <div class="play"><svg width="14" height="16"><path d="M2 1l11 7-11 7z" fill="#fff"/></svg></div>
  </div>
</section>

<footer class="footer">
  <h5 style="left:93px">Quick Links</h5>
  <ul style="left:93px"><li>Home</li><li>About us</li><li>Services</li><li>Approch</li><li>Contact Us</li></ul>
  <h5 style="left:312px">Services</h5>
  <ul style="left:312px;line-height:21px"><li>Residential</li><li>Commercial</li><li>Transportation</li><li>Gyms</li><li>Educational &amp; Daycare</li><li>Real Estate</li></ul>
  <h5 style="left:560px">Contact</h5>
  <div class="addr">Loremipsum dolar site amet<br>Glassglow200 UK<br><br><br>+2 (555) 247 6190<br><br><br>info@talquire.com</div>
  <div class="circles"><span></span><span style="background:#2aa3e0"></span><span style="background:#4a78a8"></span></div>
  <h5 style="left:795px">Location</h5>
  <div class="map" role="img" aria-label="Street map showing the office location"></div>
  <div class="copy">COPYRIGHT © 2020 <b>TALQUIRE</b>. ALL RIGHTS RESERVED.</div>
</footer>

</body>
</html>
```